Calm and Compass Health Flyer (new business startup)

One page...clear enough to be read if faxed. This mental health clinic treats depression/anxiety in kids and adults. It also treats opiate and alcohol addiction. It's in downtown Elmira, NY and the owner of the clinic is from Elmira NY, where it's located. This clinic does not take health insurance, so it charges a low rate of $75 a visit once they pay the $125 starting fee.

Target Market(s)

doctors offices, new patients

Industry/Entity Type

Doctor

Requirements
Must have
• see microsoft word document. pdf is printed on the company letterhead.
Nice to have
• a simplified map would be nice. if you can include the building it would be a plus. The same two fonts were used in the business cards and letter head (kennedy small caps boo*) and Refrigerator Delux.

```html
<!DOCTYPE html>
<html lang="en">
<head>
<meta charset="UTF-8">
<title>Calm and Compass Health Flyer</title>
<link rel="stylesheet" href="https://fonts.googleapis.com/css2?family=Roboto:wght@400;500;700;900&family=Roboto+Condensed:wght@400;700&family=Passion+One:wght@700&display=swap">
<style>
  :root {
    --orange: #f0612f;
    --blue: #1e9ad8;
    --navy: #1f3a8a;
    --pale: #d6ecf9;
    --ink: #1d1d1f;
    --yellow: #fff200;
    --white: #ffffff;
    --backdrop: #e9e9e7;
  }
  * { margin: 0; padding: 0; box-sizing: border-box; }
  html, body { width: 1200px; height: 1200px; overflow: hidden; }
  body { background: var(--backdrop); font-family: "Roboto", Arial, sans-serif; color: var(--ink); }

  .flyer {
    position: absolute; left: 180px; top: 20px;
    width: 840px; height: 1160px;
    background: var(--pale); overflow: hidden;
    box-shadow: 0 6px 24px rgba(0,0,0,.18);
  }
  .hero-photo {
    position: absolute; left: 0; top: 0; width: 840px; height: 560px;
    background: linear-gradient(180deg, #f3f8fc 0%, #c9def0 22%, #9a5a44 40%, #7a3e2c 70%, #5b3026 100%);
  }
  .bands { position: absolute; left: 0; top: 0; }

  .brand { position: absolute; left: 40px; top: 30px; display: flex; align-items: center; gap: 12px; }
  .brand-dot { width: 40px; height: 40px; border-radius: 50%; background: var(--orange); }
  .brand-text { display: flex; flex-direction: column; }
  .brand-url { font-size: 15px; color: #444; text-align: right; margin-bottom: 2px; }
  .brand-name { font-family: "Roboto Condensed", sans-serif; font-weight: 700; font-size: 27px; color: var(--orange); }

  .provider { position: absolute; left: 85px; top: 225px; color: var(--white); text-shadow: 0 2px 4px rgba(0,0,0,.55); }
  .provider-name { font-family: "Roboto Condensed", sans-serif; font-weight: 700; font-size: 42px; line-height: 1.05; }
  .provider-line { font-weight: 700; font-size: 22px; line-height: 1.45; }

  .hours-badge {
    position: absolute; left: 490px; top: 250px; width: 240px; height: 240px;
    border-radius: 50%; background: var(--orange);
    box-shadow: 0 0 0 7px var(--pale), 0 0 0 11px var(--orange);
    display: flex; flex-direction: column; align-items: center; justify-content: center;
    font-family: "Passion One", sans-serif; color: var(--yellow);
    font-size: 38px; line-height: 1; text-align: center;
    text-shadow: 0 2px 0 #6b2a10;
  }

  .ages { position: absolute; left: 80px; top: 605px; font-size: 26px; font-weight: 500; }
  .conditions { position: absolute; left: 85px; top: 665px; width: 350px; }
  .conditions h2 {
    font-family: "Roboto Condensed", sans-serif; font-weight: 700; font-size: 33px;
    color: var(--orange); border-bottom: 2px solid var(--ink); padding-bottom: 6px; margin-bottom: 14px;
  }
  .conditions p { font-size: 26px; line-height: 1.32; }

  .fees { position: absolute; left: 500px; top: 530px; width: 300px; text-align: center; }
  .fee-title { font-family: "Roboto Condensed", sans-serif; font-weight: 700; font-size: 25px; line-height: 1.35; }
  .fee-price { font-weight: 500; font-size: 44px; color: var(--orange); margin-top: 2px; line-height: 1.1; }
  .fee-rule { width: 210px; height: 2px; background: #555; margin: 14px auto 16px; }

  .motto { position: absolute; left: 95px; top: 858px; font-size: 21px; color: var(--navy); }

  .contact-bar { position: absolute; left: 0; top: 895px; width: 840px; height: 150px; background: var(--orange); }
  .contact { position: absolute; left: 60px; top: 920px; color: var(--white); font-size: 23px; line-height: 1.38; font-style: normal; }
  .map {
    position: absolute; left: 565px; top: 842px; width: 225px; height: 165px;
    background: linear-gradient(160deg, #eef0ee 0%, #e3ebe3 55%, #9fc6ea 75%, #8ab9e6 100%);
    border: 3px solid var(--white); box-shadow: 0 2px 6px rgba(0,0,0,.2);
  }
  .map-pin { position: absolute; left: 102px; top: 52px; }

  .footnote { position: absolute; left: 60px; top: 1072px; width: 720px; text-align: center; font-size: 14px; font-weight: 700; line-height: 1.4; }
</style>
</head>
<body>
  <main class="flyer">
    <div class="hero-photo" role="img" aria-label="Photograph of the brick office building that houses the clinic"></div>

    <svg class="bands" width="840" height="700" viewBox="0 0 840 700" aria-hidden="true">
      <polygon points="0,555 540,390 540,425 0,635" fill="var(--blue)"/>
      <polygon points="110,560 560,420 560,455 90,625" fill="var(--orange)"/>
      <polygon points="0,635 540,425 560,455 90,625 90,700 0,700" fill="var(--pale)"/>
      <polygon points="560,455 840,370 840,700 90,700 90,625" fill="var(--pale)"/>
    </svg>

    <header class="brand">
      <span class="brand-dot"></span>
      <div class="brand-text">
        <span class="brand-url">www.calm-compass.com</span>
        <span class="brand-name">CALM &amp; COMPASS HEALTH</span>
      </div>
    </header>

    <section class="provider">
      <div class="provider-name">DANIEL REYES</div>
      <div class="provider-line">RPA, PLLC</div>
      <div class="provider-line">Psychiatric Physician Assistant</div>
      <div class="provider-line">(PA-C, PSY-CAQ)</div>
    </section>

    <div class="hours-badge">
      <span>Monday</span>
      <span>&amp;</span>
      <span>Saturdays</span>
      <span>9-4pm</span>
    </div>

    <p class="ages">Ages:&nbsp; 6 years old and up</p>

    <section class="conditions">
      <h2>CONDITIONS TREATED:</h2>
      <p>Depression, Anxiety, PTSD<br>ADHD, Addiction, Bipolar<br>Childhood Mood Disorders</p>
    </section>

    <section class="fees">
      <div class="fee-title">PSYCHIATRIC<br>EVALUATION (45min)</div>
      <div class="fee-price">$125*</div>
      <div class="fee-rule"></div>
      <div class="fee-title">PSYCHIATRIC<br>OFFICE VISIT (15min)</div>
      <div class="fee-price">$75*</div>
    </section>

    <p class="motto">“We work for you, not the insurance companies”</p>

    <div class="contact-bar"></div>
    <address class="contact">
      T: 607-555-0142 | F: 607-555-0187<br>
      dreyes@calmcompass.net<br>
      240 W. Market #118 Brookhollow, NY 13999
    </address>

    <div class="map" role="img" aria-label="Simplified street map showing the clinic location near the river">
      <svg class="map-pin" width="18" height="26" viewBox="0 0 18 26" aria-hidden="true">
        <path d="M9 0C4 0 0 4 0 9c0 7 9 17 9 17s9-10 9-17c0-5-4-9-9-9z" fill="#e53935"/>
        <circle cx="9" cy="9" r="3.5" fill="#fff"/>
      </svg>
    </div>

    <p class="footnote">*Although we do not partner with any Health Insurance Companies at this time, a bill will be provided to<br>you at the time of service for you to submit to your insurance company.</p>
  </main>
</body>
</html>
```